Cafe Menu Required

We need a menu for our coffee shop.
I would like something very much the same as what I have attached.

I have attached a word doc with the items needed on the menu.

I have also attached our logo

I would like to print these on A3 size poster

Industry/Entity Type

Cafe

```html
<!DOCTYPE html>
<html lang="en">
<head>
<meta charset="utf-8">
<title>Pulse Corner Canteen — Menu</title>
<link rel="stylesheet" href="https://fonts.googleapis.com/css2?family=EB+Garamond:wght@400;600;700&display=swap">
<style>
  :root {
    --board-centre: #2b2b2b;
    --board-edge: #060606;
    --ink: #f2f2f2;
    --brand-red: #d8232f;
  }
  * { margin: 0; padding: 0; box-sizing: border-box; }
  html, body { width: 1200px; height: 849px; overflow: hidden; }
  body {
    font-family: "EB Garamond", Georgia, serif;
    color: var(--ink);
    font-variant-numeric: oldstyle-nums;
  }
  .menu-board {
    position: relative;
    width: 1200px;
    height: 849px;
    background: radial-gradient(ellipse at 50% 40%, var(--board-centre) 0%, #1a1a1a 55%, var(--board-edge) 100%);
  }
  .brand {
    position: absolute;
    top: 52px;
    left: 0;
    width: 100%;
    display: flex;
    justify-content: center;
    align-items: center;
    gap: 14px;
  }
  .brand-dot {
    width: 26px;
    height: 26px;
    border-radius: 50%;
    background: var(--brand-red);
  }
  .brand-name {
    font-size: 62px;
    font-weight: 700;
    line-height: 1;
    letter-spacing: 2px;
    color: var(--brand-red);
  }
  .tagline {
    position: absolute;
    top: 165px;
    left: 0;
    width: 100%;
    text-align: center;
    font-size: 23px;
    line-height: 30px;
  }
  .menu-section { position: absolute; }
  .section-title {
    font-size: 23px;
    font-weight: 700;
    line-height: 30px;
    margin-bottom: 12px;
  }
  .item-list { list-style: none; }
  .item {
    display: flex;
    justify-content: space-between;
    font-size: 24px;
    line-height: 32.5px;
    height: 32.5px;
  }
  .price { font-size: 22px; }
  .hot { top: 218px; left: 73px; width: 449px; }
  .extras { top: 218px; left: 687px; width: 443px; }
  .cold { top: 454px; left: 687px; width: 443px; }
  .cold .section-title { margin-bottom: 13px; }
  .social-handle {
    position: absolute;
    top: 755px;
    right: 70px;
    font-size: 23px;
    font-weight: 700;
    line-height: 30px;
  }
</style>
</head>
<body>
<main class="menu-board">
  <header>
    <div class="brand">
      <span class="brand-dot"></span>
      <span class="brand-name">PULSE</span>
    </div>
    <p class="tagline">coffee • catering • food to go</p>
  </header>

  <section class="menu-section hot">
    <h2 class="section-title">hot beverages</h2>
    <ul class="item-list">
      <li class="item"><span>espresso</span><span class="price">3.5</span></li>
      <li class="item"><span>piccolo</span><span class="price">3.5</span></li>
      <li class="item"><span>short macchiato</span><span class="price">4.0</span></li>
      <li class="item"><span>long macchiato</span><span class="price">4.5</span></li>
      <li class="item"><span>latte</span><span class="price">4/4.5/5.5</span></li>
      <li class="item"><span>cappucinno</span><span class="price">4/4.5/5.5</span></li>
      <li class="item"><span>flat white</span><span class="price">4/4.5/5.5</span></li>
      <li class="item"><span>long black</span><span class="price">4/4.5/5.5</span></li>
      <li class="item"><span>hot chocolate</span><span class="price">4/4.5/5.5</span></li>
      <li class="item"><span>white hot chocolate</span><span class="price">4/4.5/5.5</span></li>
      <li class="item"><span>mocha</span><span class="price">4.5/5.0/6.0</span></li>
      <li class="item"><span>white choc mocha</span><span class="price">4.5/5.0/6.0</span></li>
      <li class="item"><span>chai latte</span><span class="price">4.5/5.0/6.0</span></li>
      <li class="item"><span>dirty chai</span><span class="price">5.0/5.5/6.5</span></li>
      <li class="item"><span>selection of teas</span><span class="price">3.8</span></li>
    </ul>
  </section>

  <section class="menu-section extras">
    <h2 class="section-title">extras</h2>
    <ul class="item-list">
      <li class="item"><span>extra shot</span><span class="price">0.5</span></li>
      <li class="item"><span>decaf</span><span class="price">0.5</span></li>
      <li class="item"><span>syrups (caramel/hazelnut/vanilla)</span><span class="price">0.5</span></li>
      <li class="item"><span>soy</span><span class="price">0.5</span></li>
      <li class="item"><span>lactose free</span><span class="price">0.5</span></li>
    </ul>
  </section>

  <section class="menu-section cold">
    <h2 class="section-title">cold beverages</h2>
    <ul class="item-list">
      <li class="item"><span>iced latte</span><span class="price">4.5</span></li>
      <li class="item"><span>iced long black</span><span class="price">4.5</span></li>
      <li class="item"><span>iced coffee w/ice cream</span><span class="price">6.0</span></li>
      <li class="item"><span>iced chocolate w/ice cream</span><span class="price">6.0</span></li>
      <li class="item"><span>coffee frappe</span><span class="price">6.0</span></li>
      <li class="item"><span>mango frappe</span><span class="price">6.0</span></li>
    </ul>
  </section>

  <footer class="social-handle">@pulsecornercanteen</footer>
</main>
</body>
</html>
```